Highly motivated family winery needs new wine labels.

Company and target group:
We are a smaller, family-run winery in the heart of Germany and focus on quality rather than quantity. We primarily market to private customers, but are also represented in food retail. The wines appeal to both younger and older wine drinkers (30 – 80 years old). The labels should also be accordingly.
Requirements and wishes:
We would like to have a new logo consisting of the letters F and W that can be used in both 1 color and 2 colors. The family name “Weidlinger” should appear on the label, with the font being left to the creativity of the designers. The size of the label has not yet been fixed, but it should run around the bottle and therefore have a front and back (around 160mm wide and 80mm high). The design should be simple, modern and not too ornate.
The currently 22 types of wine/sparkling wine should all have the same label, but we would like to color-code the flavors in some way.
Perhaps the silhouette of one of the buildings of our winery (with the tower) can be incorporated into the design of the label (see picture).
A central element of the labels should have a high recognition value and be placed on the front of the label with the later wine type information.
We look forward to your suggestions.
Wegen der Weihnachtsfeiertage möchte ich das Projekt verlängern, um den Designern mehr Zeit zu geben. Bisher sind auch nur wenige Worschläge eingegangen.

```html
<!DOCTYPE html>
<html lang="en">
<head>
<meta charset="utf-8">
<title>Weidlinger Wine Label</title>
<link rel="stylesheet" href="https://fonts.googleapis.com/css2?family=Playfair+Display:wght@900&family=Oswald:wght@300&family=Open+Sans:wght@400&display=swap">
<style>
  :root {
    --paper: #ffffff;
    --label-white: #ffffff;
    --slate: #656565;
    --slate-mid: #5a5a5a;
    --gold: #a48a52;
    --ink-light: #ffffff;
  }
  html, body {
    margin: 0;
    padding: 0;
    width: 1200px;
    height: 1187px;
    overflow: hidden;
    background: var(--paper);
  }
  .canvas {
    position: relative;
    width: 1200px;
    height: 1187px;
    display: flex;
    align-items: center;
    justify-content: center;
  }
  .wine-label {
    display: block;
    width: 600px;
    height: 1130px;
  }
  .label-back { fill: var(--slate); }
  .label-front { fill: var(--label-white); }
  .label-frame { fill: none; stroke: url(#goldEdge); stroke-width: 6; }
  .brand-band { fill: url(#bandShade); }
  .info-band { fill: var(--slate-mid); }
  .family-name {
    font-family: "Playfair Display", serif;
    font-weight: 900;
    font-size: 46px;
    fill: var(--gold);
  }
  .brand-mark-dot { fill: var(--gold); }
  .brand-mark-name {
    font-family: "Playfair Display", serif;
    font-weight: 900;
    font-size: 40px;
    fill: var(--gold);
  }
  .since {
    font-family: "Open Sans", sans-serif;
    font-size: 15px;
    fill: var(--ink-light);
  }
  .volume {
    font-family: "Oswald", sans-serif;
    font-weight: 300;
    font-size: 25px;
    fill: var(--ink-light);
  }
  .volume-mark { font-size: 42px; }
  .label-note {
    font-family: "Open Sans", sans-serif;
    font-size: 14.5px;
    fill: var(--ink-light);
  }
  .tower-art { fill: var(--ink-light); }
  .grape-art { fill: var(--gold); }
</style>
</head>
<body>
<main class="canvas">
  <svg class="wine-label" viewBox="1088 376 454 854" xmlns="http://www.w3.org/2000/svg" aria-label="Weidlinger wine label">
    <defs>
      <linearGradient id="goldEdge" x1="0" y1="0" x2="1" y2="1">
        <stop offset="0" stop-color="#a07f45"/>
        <stop offset="0.35" stop-color="#f2d58d"/>
        <stop offset="0.7" stop-color="#b5965a"/>
        <stop offset="1" stop-color="#9a7c47"/>
      </linearGradient>
      <linearGradient id="bandShade" x1="0" y1="0" x2="1" y2="0">
        <stop offset="0" stop-color="#474747"/>
        <stop offset="1" stop-color="#5f5f5f"/>
      </linearGradient>
      <clipPath id="frontShape">
        <path d="M1100,590 C1095,470 1220,390 1350,388 C1480,385 1535,470 1530,590 C1528,700 1500,900 1455,1090 C1300,1080 1180,980 1130,860 C1112,790 1105,700 1100,590 Z"/>
      </clipPath>
    </defs>

    <path class="label-back" d="M1096,600 L1110,1000 C1128,1130 1250,1215 1458,1220 C1480,1100 1510,950 1528,820 L1533,600 Z"/>

    <path class="label-front" d="M1100,590 C1095,470 1220,390 1350,388 C1480,385 1535,470 1530,590 C1528,700 1500,900 1455,1090 C1300,1080 1180,980 1130,860 C1112,790 1105,700 1100,590 Z"/>

    <g clip-path="url(#frontShape)">
      <rect class="brand-band" x="1270" y="380" width="102" height="257"/>
      <rect class="info-band" x="1270" y="913" width="102" height="180"/>
    </g>

    <path class="label-frame" d="M1100,590 C1095,470 1220,390 1350,388 C1480,385 1535,470 1530,590 C1528,700 1500,900 1455,1090 C1300,1080 1180,980 1130,860 C1112,790 1105,700 1100,590 Z"/>

    <rect class="tower-art" x="1298" y="444" width="45" height="78" rx="3" role="img" aria-label="Silhouette of the winery tower building"/>

    <text class="family-name" x="1318" y="585" text-anchor="middle">Weidlinger</text>

    <g class="brand-mark">
      <circle class="brand-mark-dot" cx="1322" cy="735" r="44"/>
      <text class="brand-mark-name" x="1322" y="835" text-anchor="middle">Weidlinger</text>
    </g>

    <text class="since" x="1322" y="936" text-anchor="middle">since 1992</text>

    <rect class="grape-art" x="1300" y="966" width="44" height="68" rx="18" role="img" aria-label="Small grape cluster icon"/>

    <text class="volume" x="1172" y="1101">750 ml <tspan class="volume-mark" dy="4">℮</tspan><tspan dy="-4"> 18% vol</tspan></text>

    <text class="label-note" x="1451" y="1140" text-anchor="end">Lorem ipsum dolor sit amet, et assum</text>
    <text class="label-note" x="1451" y="1160" text-anchor="end">ignota temporibus vix.</text>
  </svg>
</main>
</body>
</html>
```